Business Card Design

I need a business card design for a new business based in South West Australia.
I specialize in residential window cleaning & general handyman maintenance.

Industry/Entity Type

Business

Contact Information for Business Card

Dale Marsh - 512 SILVER HAWK DETAILING
- Window Cleaning
- House Maintenance

```html
<!DOCTYPE html>
<html lang="en">
<head>
<meta charset="utf-8">
<title>512 Silver Hawk Detailing – Business Card</title>
<link href="https://fonts.googleapis.com/css2?family=Source+Sans+3:wght@400;600&display=swap" rel="stylesheet">
<style>
  :root {
    --stage: #000000;
    --card-front: #f3f3f3;
    --card-back: #ffffff;
    --gold: #f5b400;
    --ink: #3a3a3a;
    --muted: #6a6a6a;
  }
  * { margin: 0; padding: 0; box-sizing: border-box; }
  html, body { width: 1200px; height: 900px; overflow: hidden; background: var(--stage); }
  body { position: relative; font-family: "Source Sans 3", "Myriad Pro", sans-serif; }

  .card { position: absolute; top: 200px; width: 310px; height: 502px; }
  .card--front { left: 274px; background: var(--card-front); border-radius: 75px 0 75px 0; }
  .card--back { left: 637px; width: 309px; background: var(--card-back); border-radius: 0 75px 0 75px; }

  .front-brand { position: absolute; right: 44px; top: 74px; display: flex; flex-direction: column; align-items: flex-end; gap: 10px; }
  .brand-square { width: 50px; height: 50px; background: var(--gold); }
  .front-brand__name { font-weight: 600; font-size: 14px; color: var(--ink); letter-spacing: 0.4px; }

  .contact { position: absolute; left: 27px; top: 326px; color: var(--ink); }
  .contact__name { font-weight: 600; font-size: 18px; color: var(--gold); line-height: 22px; }
  .contact__role { font-size: 15px; line-height: 20px; }
  .contact__address { margin-top: 18px; font-size: 14.5px; line-height: 16px; }
  .contact__lines { margin-top: 11px; list-style: none; font-size: 14.5px; line-height: 20px; }
  .contact__lines li { display: flex; align-items: center; gap: 6px; }
  .contact__lines svg { width: 11px; height: 11px; fill: var(--gold); }

  .back-brand { position: absolute; left: 0; right: 0; top: 200px; text-align: center; }
  .back-brand .brand-square { width: 40px; height: 40px; margin: 0 auto 16px; }
  .back-brand__name { font-weight: 600; font-size: 18px; line-height: 24px; letter-spacing: 0.6px; color: var(--ink); }
  .back-brand__tagline { margin-top: 4px; font-size: 11px; letter-spacing: 0.4px; color: var(--muted); }
</style>
</head>
<body>
  <section class="card card--front">
    <div class="front-brand">
      <span class="brand-square"></span>
      <span class="front-brand__name">512 SILVER HAWK DETAILING</span>
    </div>
    <div class="contact">
      <p class="contact__name">DALE MARSH</p>
      <p class="contact__role">Managing Director</p>
      <p class="contact__address">512 Harbour Road<br>Bunbury WA, 6230</p>
      <ul class="contact__lines">
        <li><svg viewBox="0 0 12 12" aria-hidden="true"><path d="M1 4c0-2 2-3 5-3s5 1 5 3l-2 1-1-1.5H4L3 5zM3 6h6l1.5 5h-9z"/></svg>555-201-4417</li>
        <li><svg viewBox="0 0 12 12" aria-hidden="true"><path d="M1 3h10v7H1zM1.5 3.5 6 7l4.5-3.5" stroke="#fff" stroke-width="0.8"/></svg>hello@silverhawk.au</li>
      </ul>
    </div>
  </section>

  <section class="card card--back">
    <div class="back-brand">
      <span class="brand-square"></span>
      <p class="back-brand__name">512 SILVER HAWK DETAILING</p>
      <p class="back-brand__tagline">Residential Windows · Handyman Repairs</p>
    </div>
  </section>
</body>
</html>
```